Recipe mobile app, new flow and design for uploading recipe process

I need a new recipe upload process that's simple, intuitive, and engaging.
The goal is to have a user-friendly and fast flow.
The app is a social recipe library where anyone can upload a recipe after signing up. I currently have a flow, but it's "boring," so I'd like to significantly improve this aspect of the app.
When I create a new recipe, it's immediately saved and labeled as a draft. I'll then need to specify:
- Recipe title
- Cover image (required)
- Number of people (how many people is the recipe for)
- Ingredients (name, quantity, and unit of measurement)
- Recipe explanation (broken down into steps, and I can optionally attach an image to each step)
- Upload
Every change is immediately saved, so you can edit, exit, and resume editing later.
I've attached images of the app and the current upload process.
Thank you.
Low design quality
Good morning everyone,
some of the designs received are fantastic, but please make sure to carefully read the requirement so as not to do extra work.
The requirement is to redesign the flow that a user follows when uploading a recipe to the platform.
We have uploaded the current app screens to give you an idea of what the product looks like, what the colors and style are, but we don’t need a full redesign - only the part mentioned above, while keeping the existing style and colors (we cannot rework the entire theme).
To clarify: if you look at the screens shared in the zip file attached to the project, the focus should be on the screens from 5_.png to 10_.png.
These screens can be redesigned in the most creative way you think, as long as the overall theme remains unchanged.
Thank you for your attention.

```html
<!DOCTYPE html>
<html lang="en">
<head>
<meta charset="utf-8">
<title>New Recipe</title>
<link href="https://fonts.googleapis.com/css2?family=Noto+Sans:wght@400;500;700&family=Roboto:wght@400&display=swap" rel="stylesheet">
<style>
  :root {
    --bg: #f4f4f4;
    --field: #e0e0e0;
    --field-light: #e6e6e6;
    --ink: #1f1f1f;
    --muted: #767676;
    --hint: #a9a9a9;
    --green: #1a9e55;
    --red: #ef8a80;
    --divider: #ffffff;
    --line: #6a6a6a;
  }
  * { box-sizing: border-box; margin: 0; padding: 0; }
  html, body { width: 1200px; height: 2649px; overflow: hidden; }
  body { background: var(--bg); font-family: "Noto Sans", sans-serif; color: var(--ink); position: relative; }
  .abs { position: absolute; }

  .status-time { left: 55px; top: 12px; font-family: "Roboto", sans-serif; font-size: 38px; color: #444; }
  .status-icons { left: 985px; top: 14px; }

  .back { left: 70px; top: 130px; }
  .next-action { left: 1052px; top: 128px; font-size: 42px; font-weight: 700; color: var(--green); }

  .cover { left: 115px; top: 296px; width: 978px; height: 494px; border-radius: 44px;
    background: linear-gradient(135deg, #6b5f55 0%, #b9776a 35%, #d7786a 55%, #7d8a62 75%, #5d5a57 100%);
    box-shadow: 0 6px 18px rgba(0,0,0,.15); display: flex; align-items: center; justify-content: center; }

  .name-input { left: 144px; top: 886px; width: 920px; height: 70px; border-bottom: 2px solid var(--line);
    font-size: 40px; color: #6e6e6e; padding-left: 15px; letter-spacing: .5px; }

  .section-title { font-size: 40px; color: var(--muted); letter-spacing: .5px; }

  .ingredient { left: 160px; width: 653px; height: 88px; background: var(--field); border-radius: 16px;
    box-shadow: 0 2px 4px rgba(0,0,0,.06); }
  .ingredient .label { position: absolute; left: 39px; top: 17px; font-size: 37px; }
  .ingredient .sep { position: absolute; left: 575px; top: 10px; width: 2px; height: 68px; background: var(--divider); }
  .ingredient .remove { position: absolute; left: 597px; top: 23px; }

  .quantity { left: 834px; width: 217px; height: 88px; background: var(--field-light); border-radius: 16px; }
  .quantity .amount { position: absolute; right: 103px; top: 20px; font-size: 37px; }
  .quantity .sep { position: absolute; left: 127px; top: 10px; width: 2px; height: 68px; background: var(--divider); }
  .quantity .unit { position: absolute; left: 140px; top: 18px; font-size: 37px; }
  .quantity .caret { position: absolute; left: 186px; top: 38px; }

  .add-btn { width: 74px; height: 74px; border-radius: 50%; background: var(--green); display: flex; align-items: center; justify-content: center; }

  .unit-menu { left: 834px; top: 1373px; width: 217px; height: 243px; background: var(--field-light); border-radius: 16px; overflow: hidden; }
  .unit-menu li { list-style: none; position: absolute; left: 0; width: 100%; height: 48px; padding-left: 18px;
    font-family: "Roboto", sans-serif; font-size: 31px; line-height: 48px; color: var(--ink); }
  .unit-menu li.selected { background: #fafafa; }
  .unit-menu .scrollbar { position: absolute; left: 204px; top: 112px; width: 7px; height: 32px; background: #555; border-radius: 3px; }

  .step { left: 146px; width: 908px; height: 162px; background: var(--field); border-radius: 16px; box-shadow: 0 2px 4px rgba(0,0,0,.06); }
  .step .text { position: absolute; left: 42px; top: 14px; font-size: 33px; line-height: 45px; letter-spacing: .4px; }
  .step .placeholder { position: absolute; left: 17px; top: 16px; font-size: 33px; color: var(--hint); }
  .step .sep1 { position: absolute; left: 641px; top: 6px; width: 2px; height: 150px; background: var(--divider); }
  .step .sep2 { position: absolute; left: 831px; top: 6px; width: 2px; height: 150px; background: var(--divider); }
  .step .thumb { position: absolute; left: 655px; top: 0; width: 163px; height: 162px;
    background: linear-gradient(160deg, #4c5660, #6a5f52 50%, #b08a55 70%, #3e4650); display: flex; align-items: center; justify-content: center; }
  .step .slot { position: absolute; left: 655px; top: 0; width: 163px; height: 162px; display: flex; align-items: center; justify-content: center; }
  .step .remove { position: absolute; left: 847px; top: 59px; }

  .persons-label { left: 159px; top: 2188px; font-size: 40px; color: #6e6e6e; letter-spacing: .5px; }
  .persons-box { left: 930px; top: 2173px; width: 121px; height: 85px; background: var(--field); border-radius: 14px;
    font-family: "Roboto", sans-serif; font-size: 40px; text-align: center; line-height: 85px; }

  .home-indicator { left: 446px; top: 2611px; width: 314px; height: 10px; border-radius: 5px; background: #3a3a3a; }
</style>
</head>
<body>
  <div class="abs status-time">3:43</div>
  <svg class="abs" style="left:152px;top:22px" width="28" height="30" viewBox="0 0 28 30"><rect x="1" y="1" width="26" height="28" rx="3" fill="#444"/><text x="14" y="23" font-family="Roboto, sans-serif" font-size="20" font-weight="700" fill="#f4f4f4" text-anchor="middle">A</text></svg>
  <svg class="abs status-icons" width="130" height="46" viewBox="0 0 130 46">
    <path d="M2 10 Q25 -6 48 10 L25 40 Z" fill="#444"/>
    <path d="M90 6 L90 44 L52 44 Z" fill="none" stroke="#444" stroke-width="3"/>
    <rect x="106" y="6" width="20" height="38" rx="3" fill="#444"/>
  </svg>

  <svg class="abs back" width="40" height="56" viewBox="0 0 40 56"><path d="M30 6 L8 28 L30 50" fill="none" stroke="#111" stroke-width="5" stroke-linecap="round" stroke-linejoin="round"/></svg>
  <div class="abs next-action">Next</div>

  <div class="abs cover" role="img" aria-label="Cover photo: chef plating sliced meat and green salad on a cutting board">
    <svg width="100" height="100" viewBox="0 0 100 100" fill="none" stroke="#333" stroke-width="5" stroke-linecap="round" stroke-linejoin="round" opacity=".8">
      <path d="M60 10 H25 Q10 10 10 25 V75 Q10 90 25 90 H75 Q90 90 90 75 V45"/>
      <circle cx="35" cy="35" r="8"/>
      <path d="M12 78 L38 56 L60 72 L90 55"/>
      <path d="M78 6 V30 M66 18 H90"/>
    </svg>
  </div>

  <div class="abs name-input">Add Your Recipe Name Here!</div>

  <div class="abs section-title" style="left:146px;top:1048px">Recipe Ingredients</div>

  <div class="abs ingredient" style="top:1133px">
    <span class="label">Item 01</span><span class="sep"></span>
    <svg class="remove" width="42" height="42" viewBox="0 0 42 42"><circle cx="21" cy="21" r="19" fill="none" stroke="var(--red)" stroke-width="2.5"/><path d="M11 21 H31" stroke="var(--red)" stroke-width="2.5"/></svg>
  </div>
  <div class="abs quantity" style="top:1133px">
    <span class="amount">250</span><span class="sep"></span><span class="unit">g</span>
    <svg class="caret" width="22" height="14" viewBox="0 0 22 14"><path d="M2 2 H20 L11 12 Z" fill="#666"/></svg>
  </div>

  <div class="abs ingredient" style="top:1266px">
    <span class="label">Item 02</span><span class="sep"></span>
    <svg class="remove" width="42" height="42" viewBox="0 0 42 42"><circle cx="21" cy="21" r="19" fill="none" stroke="var(--red)" stroke-width="2.5"/><path d="M11 21 H31" stroke="var(--red)" stroke-width="2.5"/></svg>
  </div>
  <div class="abs quantity" style="top:1266px">
    <span class="amount">1</span><span class="sep"></span><span class="unit">ml</span>
    <svg class="caret" width="22" height="14" viewBox="0 0 22 14"><path d="M2 12 H20 L11 2 Z" fill="#666"/></svg>
  </div>

  <div class="abs add-btn" style="left:569px;top:1399px">
    <svg width="44" height="44" viewBox="0 0 44 44"><circle cx="22" cy="22" r="18" fill="none" stroke="#fff" stroke-width="3.5"/><path d="M22 13 V31 M13 22 H31" stroke="#fff" stroke-width="3.5" stroke-linecap="round"/></svg>
  </div>

  <ul class="abs unit-menu">
    <li style="top:16px">kilogram (kg)</li>
    <li class="selected" style="top:82px">mililiter (ml)</li>
    <li style="top:144px">gram (g)</li>
    <li style="top:207px">pieces (pcs)</li>
    <span class="scrollbar"></span>
  </ul>

  <div class="abs section-title" style="left:145px;top:1560px">Steps</div>

  <div class="abs step" style="top:1646px">
    <p class="text">Add main ingredients<br>also remove heater<br>add sugar</p>
    <span class="sep1"></span>
    <div class="thumb" role="img" aria-label="Step photo: pan with food cooking">
      <svg width="100" height="100" viewBox="0 0 100 100" fill="none" stroke="#222" stroke-width="5" stroke-linecap="round" stroke-linejoin="round" opacity=".75">
        <path d="M60 10 H25 Q10 10 10 25 V75 Q10 90 25 90 H75 Q90 90 90 75 V45"/><circle cx="35" cy="35" r="8"/><path d="M12 78 L38 56 L60 72 L90 55"/><path d="M78 6 V30 M66 18 H90"/>
      </svg>
    </div>
    <span class="sep2"></span>
    <svg class="remove" width="42" height="42" viewBox="0 0 42 42"><circle cx="21" cy="21" r="19" fill="none" stroke="var(--red)" stroke-width="2.5"/><path d="M11 21 H31" stroke="var(--red)" stroke-width="2.5"/></svg>
  </div>

  <div class="abs step" style="top:1844px">
    <span class="placeholder">Step 02</span>
    <span class="sep1"></span>
    <div class="slot">
      <svg width="100" height="100" viewBox="0 0 100 100" fill="none" stroke="#555" stroke-width="5" stroke-linecap="round" stroke-linejoin="round">
        <path d="M60 10 H25 Q10 10 10 25 V75 Q10 90 25 90 H75 Q90 90 90 75 V45"/><circle cx="35" cy="35" r="8"/><path d="M12 78 L38 56 L60 72 L90 55"/><path d="M78 6 V30 M66 18 H90"/>
      </svg>
    </div>
    <span class="sep2"></span>
    <svg class="remove" width="42" height="42" viewBox="0 0 42 42"><circle cx="21" cy="21" r="19" fill="none" stroke="var(--red)" stroke-width="2.5"/><path d="M11 21 H31" stroke="var(--red)" stroke-width="2.5"/></svg>
  </div>

  <div class="abs add-btn" style="left:569px;top:2046px">
    <svg width="44" height="44" viewBox="0 0 44 44"><circle cx="22" cy="22" r="18" fill="none" stroke="#fff" stroke-width="3.5"/><path d="M22 13 V31 M13 22 H31" stroke="#fff" stroke-width="3.5" stroke-linecap="round"/></svg>
  </div>

  <div class="abs persons-label">For How Many Persons this recipe</div>
  <div class="abs persons-box">4</div>

  <div class="abs home-indicator"></div>
</body>
</html>
```